I would like a single page website for Skylark Rentals Australia. In the file list provided there is basic information to be included as well as our logo with colors, fonts and images to be included.
Site must be very simple and be able to be loaded onto smart phones etc very quickly.
Site needs to be very smart in appearance

Target Market(s)

All prospective drone customers from Police to Parties.

Industry/Entity Type

Hire

Coding

Coded - Design and coding required

Number of Pages Required

1 page

Requirements
Must have
• Must have variation of color schemes supplied
Nice to have
• Must be very eye catching without going over the top
Should not have
• Anything slow to load.

```html
<!DOCTYPE html>
<html lang="en">
<head>
<meta charset="utf-8">
<title>Skylark Rentals Australia</title>
<link href="https://fonts.googleapis.com/css2?family=Open+Sans:wght@300;400;600;700;800&display=swap" rel="stylesheet">
<style>
:root{
  --green:#8dc63f;
  --green-dark:#5f8f24;
  --green-light:#b5dc78;
  --ink:#333333;
  --charcoal:#2f2f2f;
  --panel:#3a3a3a;
  --grey:#f0f0f0;
  --muted:#777777;
  --white:#ffffff;
}
*{margin:0;padding:0;box-sizing:border-box}
html,body{width:1200px;height:4128px;overflow:hidden}
body{font-family:"Open Sans",Arial,sans-serif;color:var(--ink);background:var(--white);position:relative}
section,header,footer{position:absolute;left:0;width:1200px;overflow:hidden}
.abs{position:absolute}

/* header */
.site-header{top:0;height:56px;background:var(--panel);z-index:5}
.brand-name{position:absolute;left:80px;top:17px;color:var(--green);font-size:16px;font-weight:700;line-height:22px;white-space:nowrap}
.menu-btn{position:absolute;right:96px;top:6px;width:44px;height:44px;background:var(--green);display:flex;flex-direction:column;justify-content:center;align-items:center;gap:5px}
.menu-btn span{width:22px;height:3px;background:var(--white)}

/* hero */
.hero{top:56px;height:552px;background:linear-gradient(160deg,#6d7a82 0%,#4a5560 40%,#2d343a 100%)}
.hero-photo{position:absolute;inset:0;background:linear-gradient(180deg,rgba(200,210,220,.35) 0%,rgba(40,45,50,.2) 60%,rgba(20,20,20,.5) 100%)}
.hero-title{left:88px;top:210px;font-size:72px;font-weight:700;color:var(--white);letter-spacing:1px}
.hero-text{left:88px;top:318px;width:470px;font-size:14px;line-height:20px;color:#e8e8e8}
.btn-outline{left:88px;top:388px;height:40px;padding:0 46px 0 16px;border:2px solid var(--white);color:var(--white);font-size:14px;line-height:36px}
.btn-outline i{position:absolute;right:10px;top:8px;width:20px;height:20px;border:2px solid var(--white);border-radius:50%}
.drone{background:radial-gradient(ellipse at center,#ffffff 0%,#e6e6e6 45%,rgba(200,200,200,.0) 72%)}

/* about */
.about{top:608px;height:612px;background:var(--grey)}
.video-diamond{left:60px;top:150px;width:420px;height:420px;transform:rotate(45deg);background:linear-gradient(135deg,var(--green-light),var(--green) 55%,var(--green-dark))}
.play{width:64px;height:64px;border:4px solid var(--white);border-radius:50%}
.play::after{content:"";position:absolute;left:22px;top:15px;border-left:20px solid var(--white);border-top:13px solid transparent;border-bottom:13px solid transparent}
.section-title{font-size:72px;font-weight:700;line-height:1}
.about-title{left:600px;top:124px;color:var(--green)}
.rule{height:2px;background:var(--green)}
.body-copy{font-size:14px;line-height:20px}
.about-copy{left:600px;top:212px;width:520px;color:#555}
.ghost-diamond{width:104px;height:104px;background:var(--white);transform:rotate(45deg);opacity:.8}
.marker{width:44px;height:44px;transform:rotate(45deg);display:flex;align-items:center;justify-content:center}
.marker span{width:14px;height:14px;border:3px solid currentColor;border-radius:50%;transform:rotate(-45deg)}
.marker.green{background:var(--green);color:var(--white)}
.marker.white{background:var(--white);color:var(--ink)}

/* think */
.think{top:1220px;height:620px;background:linear-gradient(135deg,#1f1f1f 0%,#4a4a4a 55%,#2a2a2a 100%)}
.think-title{left:600px;top:212px;color:var(--white)}
.think-title small{font-size:24px;font-weight:300;letter-spacing:1px}
.think-copy{left:600px;top:300px;width:540px;color:#dddddd}

/* experience */
.experience{top:1840px;height:1140px;background:var(--ink)}
.exp-title{left:0;width:1200px;top:80px;text-align:center;color:var(--white);font-size:68px}
.exp-rule{left:440px;top:160px;width:320px;height:2px;background:#666}
.exp-copy{left:260px;top:178px;width:680px;text-align:center;color:#bbbbbb}
.icon-diamond{width:112px;height:112px;background:var(--green);transform:rotate(45deg);display:flex;align-items:center;justify-content:center}
.icon-diamond svg{transform:rotate(-45deg)}
.thumb{width:336px;height:208px;display:flex;align-items:center;justify-content:center}
.thumb .play{position:relative;border-color:var(--green)}
.thumb .play::after{border-left-color:var(--green)}

/* laboratory */
.lab{top:2980px;height:640px;background:var(--white)}
.lab-title{left:0;width:600px;top:120px;text-align:center;color:var(--ink)}
.lab-copy{left:90px;top:214px;width:600px;text-align:center;color:#666}
.spec-label{font-size:12px;letter-spacing:1px;color:#666;font-weight:600}
.spec-value{font-size:56px;font-weight:600;color:var(--green);line-height:1}
.spec-value small{font-size:24px}
.spec-rule{height:1px;background:#cccccc;width:220px}
.right{text-align:right}

/* partners */
.partners{top:3620px;height:280px;background:linear-gradient(180deg,#55585a 0%,#2e3134 45%,#1d2022 100%)}
.partner-row{left:80px;top:108px;width:1040px;display:flex;justify-content:space-between;align-items:center}
.partner{font-size:34px;font-weight:700;color:var(--white)}

/* footer */
.site-footer{top:3900px;height:228px;background:var(--white)}
.footer-name{left:0;width:1200px;top:72px;text-align:center;color:var(--green);font-size:22px;font-weight:700;line-height:30px}
.copyright{left:0;width:1200px;top:128px;text-align:center;font-size:11px;color:#999;letter-spacing:1px}
</style>
</head>
<body>

<header class="site-header">
  <div class="brand-name">Skylark Rentals Australia</div>
  <div class="menu-btn" aria-label="Menu"><span></span><span></span><span></span></div>
</header>

<section class="hero">
  <div class="hero-photo" role="img" aria-label="Snow-capped mountain range under a hazy sky"></div>
  <svg class="abs" style="left:0;top:0" width="1200" height="552" viewBox="0 0 1200 552" aria-hidden="true">
    <polygon points="740,0 880,0 720,552 580,552" fill="#8dc63f"/>
    <polygon points="900,0 1000,0 840,552 740,552" fill="#ffffff" opacity=".12"/>
    <polygon points="1020,0 1200,0 1200,120 1000,552 880,552" fill="#5a5a5a" opacity=".55"/>
  </svg>
  <div class="abs drone" style="left:600px;top:20px;width:560px;height:460px" role="img" aria-label="White camera drone with gimbal, hovering"></div>
  <h1 class="abs hero-title">TAKE FLIGHT</h1>
  <p class="abs hero-text body-copy">Aerial filming, mapping and event coverage across Australia, with certified pilots and ready-to-fly kits for every job.</p>
  <div class="abs btn-outline">Read More<i></i></div>
</section>

<section class="about">
  <div class="abs video-diamond" role="img" aria-label="Aerial view of green farmland inside a diamond frame"></div>
  <div class="abs play" style="left:238px;top:328px"></div>
  <h2 class="abs section-title about-title">ABOUT US</h2>
  <div class="abs rule" style="left:600px;top:200px;width:520px"></div>
  <p class="abs body-copy about-copy">We supply professional drones for hire to police, film crews, farmers, builders and party planners. Every unit is serviced, insured and delivered fully charged, so you can fly on the day without the worry. Our team helps you choose the right craft and plan each flight safely.</p>
  <div class="abs ghost-diamond" style="left:320px;top:460px"></div>
  <div class="abs ghost-diamond" style="left:480px;top:460px"></div>
  <div class="abs ghost-diamond" style="left:640px;top:460px"></div>
  <div class="abs ghost-diamond" style="left:800px;top:460px"></div>
  <div class="abs ghost-diamond" style="left:960px;top:460px"></div>
  <div class="abs marker green" style="left:578px;top:542px"><span></span></div>
</section>

<section class="think">
  <div class="abs" style="inset:0;background:linear-gradient(90deg,rgba(0,0,0,.2),rgba(90,90,90,.25))" role="img" aria-label="Dark aerial photograph of a rugged coastline"></div>
  <svg class="abs" style="left:0;top:0" width="1200" height="620" viewBox="0 0 1200 620" aria-hidden="true">
    <polygon points="0,0 230,0 500,620 0,620" fill="#ffffff" opacity=".9"/>
    <polygon points="240,0 420,0 700,620 510,620" fill="#8dc63f"/>
    <polygon points="170,0 240,0 510,620 440,620" fill="#b5dc78"/>
  </svg>
  <div class="abs drone" style="left:20px;top:60px;width:380px;height:360px" role="img" aria-label="White camera drone shown from the side"></div>
  <h2 class="abs section-title think-title">THINK <small>DIFFERENT</small></h2>
  <p class="abs body-copy think-copy">From crowded festivals to remote survey sites, a fresh view from above changes what you can see. Our pilots bring stable, high resolution footage that turns ordinary moments into stories worth sharing with everyone.</p>
  <div class="abs marker white" style="left:578px;top:550px"><span></span></div>
</section>

<section class="experience">
  <h2 class="abs section-title exp-title">EXPERIENCE</h2>
  <div class="abs exp-rule"></div>
  <p class="abs body-copy exp-copy">Our drones have flown over sporting events, city skylines, building sites, crowds and family celebrations, capturing each moment with sharp, steady footage from the air.</p>

  <div class="abs icon-diamond" style="left:136px;top:304px"><svg width="48" height="48" viewBox="0 0 48 48" fill="none" stroke="#fff" stroke-width="3"><rect x="8" y="14" width="32" height="22" rx="3"/><circle cx="24" cy="25" r="6"/></svg></div>
  <div class="abs icon-diamond" style="left:336px;top:304px"><svg width="48" height="48" viewBox="0 0 48 48" fill="none" stroke="#fff" stroke-width="3"><circle cx="24" cy="24" r="16"/><path d="M24 8v32M8 24h32"/></svg></div>
  <div class="abs icon-diamond" style="left:536px;top:304px"><svg width="48" height="48" viewBox="0 0 48 48" fill="none" stroke="#fff" stroke-width="3"><rect x="6" y="20" width="26" height="14"/><path d="M32 24h8l4 6v4H32"/><circle cx="14" cy="36" r="3"/><circle cx="36" cy="36" r="3"/></svg></div>
  <div class="abs icon-diamond" style="left:736px;top:304px"><svg width="48" height="48" viewBox="0 0 48 48" fill="none" stroke="#fff" stroke-width="3"><path d="M12 8v32M36 8v32M12 18h24M12 30h24"/></svg></div>
  <div class="abs icon-diamond" style="left:936px;top:304px"><svg width="48" height="48" viewBox="0 0 48 48" fill="none" stroke="#fff" stroke-width="3"><path d="M10 22h28M14 22a10 10 0 0 1 20 0"/><rect x="16" y="26" width="16" height="14"/></svg></div>
  <div class="abs icon-diamond" style="left:236px;top:416px"><svg width="48" height="48" viewBox="0 0 48 48" fill="none" stroke="#fff" stroke-width="3"><rect x="8" y="18" width="12" height="22"/><rect x="22" y="8" width="18" height="32"/></svg></div>
  <div class="abs icon-diamond" style="left:436px;top:416px"><svg width="48" height="48" viewBox="0 0 48 48" fill="none" stroke="#fff" stroke-width="3"><circle cx="24" cy="28" r="10"/><circle cx="14" cy="14" r="4"/><circle cx="34" cy="14" r="4"/></svg></div>
  <div class="abs icon-diamond" style="left:636px;top:416px"><svg width="48" height="48" viewBox="0 0 48 48" fill="none" stroke="#fff" stroke-width="3"><path d="M6 28l14-4 10-14 4 4-6 12 14 4-14 4-6 6"/></svg></div>
  <div class="abs icon-diamond" style="left:836px;top:416px"><svg width="48" height="48" viewBox="0 0 48 48" fill="none" stroke="#fff" stroke-width="3"><path d="M8 24L24 10l16 14M14 20v20h20V20"/></svg></div>

  <div class="abs thumb" style="left:88px;top:608px;background:linear-gradient(135deg,#3b5d8a,#a33b3b 55%,#d8d8d8)" role="img" aria-label="Race cars lined up on a track, seen from above"><div class="play"></div></div>
  <div class="abs thumb" style="left:432px;top:608px;background:linear-gradient(135deg,#8a6a4a,#5a4a3c 50%,#a08070)" role="img" aria-label="Crowd gathered in a town square from above"><div class="play"></div></div>
  <div class="abs thumb" style="left:776px;top:608px;background:linear-gradient(135deg,#8fa0b0,#5a6670 50%,#b0b8c0)" role="img" aria-label="City skyline with tall towers"><div class="play"></div></div>
  <div class="abs thumb" style="left:88px;top:824px;background:linear-gradient(180deg,#6a4a4a,#8a3a3a 40%,#3f7a3a)" role="img" aria-label="Football stadium with green pitch"><div class="play"></div></div>
  <div class="abs thumb" style="left:432px;top:824px;background:linear-gradient(135deg,#b0a890,#7a7060 50%,#c8bfa8)" role="img" aria-label="Construction site with cranes"><div class="play"></div></div>
  <div class="abs thumb" style="left:776px;top:824px;background:linear-gradient(135deg,#d0d0d0,#707070 50%,#bdbdbd)" role="img" aria-label="Runners crossing a city bridge"><div class="play"></div></div>

  <div class="abs marker white" style="left:578px;top:1090px"><span></span></div>
</section>

<section class="lab">
  <svg class="abs" style="left:0;top:0" width="1200" height="640" viewBox="0 0 1200 640" aria-hidden="true">
    <polygon points="820,0 1000,0 740,640 560,640" fill="#8dc63f"/>
    <polygon points="1000,0 1080,0 820,640 740,640" fill="#b5dc78"/>
    <polygon points="1080,0 1200,0 1200,640 820,640" fill="#6b6b6b"/>
  </svg>
  <h2 class="abs section-title lab-title">LABRATORY</h2>
  <div class="abs" style="left:160px;top:198px;width:280px;height:2px;background:#ccc"></div>
  <p class="abs body-copy lab-copy">Every craft in our fleet is tested in the lab before it leaves the hangar, so you know the exact specs you are getting.</p>

  <div class="abs drone" style="left:280px;top:220px;width:600px;height:390px" role="img" aria-label="White camera drone front view"></div>

  <div class="abs spec-label" style="left:88px;top:306px">MAX PAYLOAD</div>
  <div class="abs spec-value" style="left:88px;top:330px">4.3 <small>kg</small></div>
  <div class="abs spec-rule" style="left:88px;top:400px"></div>
  <div class="abs spec-label" style="left:88px;top:424px">DRONE LENGTH</div>
  <div class="abs spec-value" style="left:88px;top:448px">70 <small>cm</small></div>
  <div class="abs spec-rule" style="left:88px;top:518px"></div>

  <div class="abs spec-label right" style="left:892px;width:220px;top:306px;color:#fff">FLIGHT DISTANCE</div>
  <div class="abs spec-value right" style="left:892px;width:220px;top:330px;color:#fff">320 <small>m</small></div>
  <div class="abs spec-rule" style="left:892px;top:400px;background:#aaa"></div>
  <div class="abs spec-label right" style="left:892px;width:220px;top:424px;color:#fff">TOTAL TIME</div>
  <div class="abs spec-value right" style="left:892px;width:220px;top:448px;color:#fff">60 <small>min</small></div>
  <div class="abs spec-rule" style="left:892px;top:518px;background:#aaa"></div>
</section>

<section class="partners">
  <div class="abs" style="inset:0" role="img" aria-label="Dark wooden boardwalk stretching to the horizon"></div>
  <div class="abs partner-row">
    <span class="partner">Kestrel</span>
    <span class="partner">Northway</span>
    <span class="partner">Orbitex</span>
    <span class="partner">Gridline</span>
    <span class="partner">Chronicle</span>
  </div>
</section>

<footer class="site-footer">
  <div class="abs footer-name">Skylark Rentals Australia</div>
  <p class="abs copyright">COPYRIGHT 2016 . ALL RIGHTS RESERVED</p>
</footer>

</body>
</html>
```